Business Cards for a start up company

We are looking for a business card design for a start up company based in Ohio. The logo is attached. We are a healthcare company. We are open to all designs but want something professional but fun; creative, not boring

Industry/Entity Type

Healthcare

```html
<!DOCTYPE html>
<html lang="en">
<head>
<meta charset="utf-8">
<title>Harbor Care Plus – Business Card</title>
<link rel="stylesheet" href="https://fonts.googleapis.com/css2?family=Questrial&family=Didact+Gothic&display=swap">
<style>
  :root {
    --navy: #27235e;
    --navy-deep: #1f1b52;
    --ink: #2b2b3a;
    --paper: #ffffff;
    --paper-shade: #ececef;
    --green: #6aa431;
    --blue: #2aa3c6;
    --backdrop: #e6e4df;
  }
  * { box-sizing: border-box; margin: 0; padding: 0; }
  html, body { width: 1200px; height: 800px; overflow: hidden; }
  body {
    background: var(--backdrop);
    font-family: "Questrial", "Didact Gothic", sans-serif;
    display: flex;
    align-items: center;
    justify-content: center;
    gap: 60px;
  }
  .card {
    position: relative;
    width: 520px;
    height: 297px;
    border-radius: 3px;
    overflow: hidden;
    box-shadow: 0 10px 28px rgba(30, 25, 60, 0.22);
  }

  /* Back side */
  .card--back {
    background: var(--navy);
    color: var(--paper);
    display: flex;
    flex-direction: column;
    align-items: center;
    justify-content: center;
  }
  .brand {
    display: flex;
    align-items: center;
    gap: 16px;
    margin-top: -10px;
  }
  .brand__dot {
    width: 44px; height: 44px;
    border-radius: 50%;
    background: var(--paper);
  }
  .brand__name {
    font-size: 34px;
    letter-spacing: 0.5px;
    color: var(--paper);
  }
  .website {
    position: absolute;
    right: 34px;
    bottom: 30px;
    font-size: 11px;
    letter-spacing: 3.5px;
    color: #c9c7e6;
  }
  .website strong { font-weight: 400; color: var(--paper); }

  /* Front side */
  .card--front {
    background: linear-gradient(160deg, var(--paper) 0%, var(--paper) 45%, var(--paper-shade) 100%);
    color: var(--ink);
  }
  .rule-top {
    position: absolute;
    left: 90px; right: 40px; top: 92px;
    height: 1.5px;
    background: var(--navy);
  }
  .name-marker {
    position: absolute;
    left: 0; top: 150px;
    width: 14px; height: 34px;
    background: var(--navy);
  }
  .person {
    position: absolute;
    left: 28px; top: 148px;
    color: var(--navy);
  }
  .person__first { font-size: 19px; font-weight: 700; letter-spacing: 0.5px; line-height: 1.05; font-family: "Didact Gothic", sans-serif; -webkit-text-stroke: 0.5px var(--navy); }
  .person__last { font-size: 19px; letter-spacing: 0.5px; line-height: 1.15; }
  .rule-name {
    position: absolute;
    left: 28px; top: 202px;
    width: 150px; height: 1.5px;
    background: var(--navy);
  }
  .person__title {
    position: absolute;
    left: 28px; top: 214px;
    font-size: 9px;
    letter-spacing: 0.6px;
  }
  .contact {
    position: absolute;
    left: 330px; top: 106px;
    font-size: 10.5px;
    line-height: 1.4;
  }
  .contact__row { display: flex; gap: 10px; }
  .contact__label { width: 40px; color: var(--navy); }
  .contact__value--link { color: var(--navy); }
  .office {
    position: absolute;
    left: 330px; top: 170px;
    font-size: 10.5px;
    line-height: 1.35;
  }
  .office__company {
    font-size: 9.5px;
    letter-spacing: 0.5px;
    color: var(--navy);
    font-weight: 700;
    -webkit-text-stroke: 0.3px var(--navy);
  }
  .stripe {
    position: absolute;
    left: 0; right: 0; bottom: 0;
    height: 10px;
    display: flex;
  }
  .stripe__navy { flex: 0 0 58%; background: var(--navy); }
  .stripe__green { flex: 0 0 18%; background: var(--green); }
  .stripe__blue { flex: 1; background: var(--blue); }
</style>
</head>
<body>

  <section class="card card--back" aria-label="Card back">
    <div class="brand">
      <span class="brand__dot"></span>
      <span class="brand__name">Harbor Care Plus</span>
    </div>
    <p class="website">WWW.<strong>HARBORCAREPLUS</strong>.COM</p>
  </section>

  <section class="card card--front" aria-label="Card front">
    <div class="rule-top"></div>
    <div class="name-marker"></div>
    <div class="person">
      <p class="person__first">MARA</p>
      <p class="person__last">ELLISON</p>
    </div>
    <div class="rule-name"></div>
    <p class="person__title">PRESIDENT DIRECTOR</p>

    <div class="contact">
      <p class="contact__row"><span class="contact__label">email:</span><span class="contact__value--link">hello@harborcare.co</span></p>
      <p class="contact__row"><span class="contact__label">direct:</span><span>+1 614 555 0182</span></p>
      <p class="contact__row"><span class="contact__label">mobile:</span><span>614/555.0147</span></p>
    </div>

    <div class="office">
      <p class="office__company">HARBOR CARE PLUS</p>
      <p>4180 Linden Park Ave, Suite 210</p>
      <p>Columbus, OH 43215</p>
    </div>

    <div class="stripe">
      <span class="stripe__navy"></span>
      <span class="stripe__green"></span>
      <span class="stripe__blue"></span>
    </div>
  </section>

</body>
</html>
```